Velvetorchid Hair & Beauty Business Card

Velvetorchid Hair & Beauty is a boutique salon located in the picturesque Lake Waiteranga NZ. The salon is very luxurious, opulent gold gilded mirrors, chandelier lit, contemporary french decor, sets the mood to create beautiful hair, makeup and all beauty services. Just had a new logo design and now after a new business card.
Logo
14 Kerewhenua Street
Waiteranga
Phone (07) 384 6139
www.velvetorchid.co.nz
email hair@velvetorchid.co.nz
Lorinda Feltham
Also need a space to put in Stylist name, date, appointment time. thanks;)
Another idea is we could incorporate the wallpaper in the back ground either on the back or front or use an ornate glided frame (around the edge of the card) like on my website where my brides photos flash.
Decided against the wall paper but at least you can see our colour theme for the salon.
Updates

Please check out my updated brief . Thanks :)

Target Market(s)

25-60 years plus, mainly mid age females , wanting the best possible service , high standard of workmanship and money not a problem.

Industry/Entity Type

Boutique

Requirements
Must have
• Gold and silver

```html
<!DOCTYPE html>
<html lang="en">
<head>
<meta charset="utf-8">
<title>Velvetorchid Hair &amp; Beauty – Business Card</title>
<link rel="stylesheet" href="https://fonts.googleapis.com/css2?family=Questrial&display=swap">
<style>
  :root {
    --page: #ece8e1;
    --gold: #b29a30;
    --gold-light: #c3ab42;
    --gold-dark: #9c8526;
    --silver: #8c8c8c;
    --paper: #f7f7f5;
    --white: #ffffff;
    --shadow: rgba(60, 45, 20, 0.25);
  }
  * { box-sizing: border-box; margin: 0; padding: 0; }
  html, body { width: 1200px; height: 1023px; overflow: hidden; }
  body {
    background: var(--page);
    font-family: "Questrial", "Century Gothic", sans-serif;
    position: relative;
  }
  .card {
    position: absolute;
    width: 540px;
    height: 309px;
    top: 357px;
    box-shadow: 0 10px 28px var(--shadow);
    overflow: hidden;
  }
  .card--front { left: 40px; }
  .card--back { left: 620px; }

  /* Front */
  .front__top {
    position: absolute; left: 0; top: 0; width: 100%; height: 138px;
    background: linear-gradient(180deg, var(--white), var(--paper));
  }
  .front__band {
    position: absolute; left: 0; top: 138px; width: 100%; height: 171px;
    background: radial-gradient(ellipse at 40% 40%, var(--gold-light), var(--gold) 60%, var(--gold-dark));
  }
  .wordmark { position: absolute; white-space: nowrap; }
  .wordmark__name { display: block; font-size: 44px; letter-spacing: 0.5px; line-height: 1; }
  .wordmark__tag { display: block; font-size: 11px; letter-spacing: 2px; text-transform: uppercase; }
  .front__wordmark { left: 0; right: 0; top: 34px; color: var(--silver); text-align: center; }
  .front__wordmark .wordmark__tag {
    display: flex; align-items: center; justify-content: center; gap: 14px; margin-top: 6px;
  }
  .front__rule { display: inline-block; width: 80px; height: 1px; background: var(--gold); }

  .address {
    position: absolute; right: 26px; top: 14px; text-align: right;
    color: var(--white); font-size: 12px; line-height: 1.5; letter-spacing: 0.5px;
  }
  .holder {
    position: absolute; left: 34px; top: 170px;
    color: var(--white); font-size: 24px; display: flex; align-items: center; gap: 10px;
  }
  .holder__dot { width: 8px; height: 8px; border-radius: 50%; background: var(--white); }
  .contacts {
    position: absolute; left: 34px; bottom: 20px; list-style: none;
    color: var(--white); font-size: 12px; line-height: 1.55; letter-spacing: 0.5px;
  }
  .contacts__label { display: inline-block; width: 30px; }

  /* Back */
  .card--back {
    background: radial-gradient(ellipse at 55% 40%, var(--gold-light), var(--gold) 55%, var(--gold-dark));
  }
  .back__rule { position: absolute; left: 30px; width: 190px; top: 108px; height: 1px; background: var(--white); }
  .back__wordmark { right: 30px; top: 118px; color: var(--white); text-align: right; }
  .back__wordmark .wordmark__tag {
    display: flex; align-items: center; justify-content: flex-end; gap: 10px; margin-top: 6px;
  }
  .back__tag-rule { display: inline-block; width: 60px; height: 1px; background: var(--white); }

  .appointment { position: absolute; left: 30px; top: 196px; width: 480px; color: var(--white); font-size: 12px; }
  .appointment__row { display: flex; gap: 22px; margin-bottom: 10px; }
  .field { display: flex; align-items: flex-end; gap: 6px; }
  .field__line { display: inline-block; height: 1px; background: rgba(255,255,255,0.75); margin-bottom: 3px; }
  .field--wide .field__line { width: 210px; }
  .field--date .field__line { width: 170px; }
  .field--time .field__line { width: 150px; }
</style>
</head>
<body>
  <section class="card card--front" aria-label="Business card front">
    <div class="front__top">
      <div class="wordmark front__wordmark">
        <span class="wordmark__name">Velvetorchid</span>
        <span class="wordmark__tag"><span class="front__rule"></span>Hair &amp; Beauty<span class="front__rule"></span></span>
      </div>
    </div>
    <div class="front__band">
      <p class="address">14 Kerewhenua Street<br>Waiteranga</p>
    </div>
    <p class="holder"><span class="holder__dot"></span>Lorinda Feltham</p>
    <ul class="contacts">
      <li><span class="contacts__label">[P]</span>(07) 384 6139</li>
      <li><span class="contacts__label">[W]</span>www.velvetorchid.co.nz</li>
      <li><span class="contacts__label">[E]</span>hair@velvetorchid.co.nz</li>
    </ul>
  </section>

  <section class="card card--back" aria-label="Appointment card back">
    <span class="back__rule"></span>
    <div class="wordmark back__wordmark">
      <span class="wordmark__name">Velvetorchid</span>
      <span class="wordmark__tag">Hair &amp; Beauty<span class="back__tag-rule"></span></span>
    </div>
    <div class="appointment">
      <div class="appointment__row"><span class="field field--wide">Stylist :<span class="field__line"></span></span></div>
      <div class="appointment__row"><span class="field field--date">Date :<span class="field__line"></span></span><span class="field field--time">Time :<span class="field__line"></span></span></div>
      <div class="appointment__row"><span class="field field--date">Date :<span class="field__line"></span></span><span class="field field--time">Time :<span class="field__line"></span></span></div>
      <div class="appointment__row"><span class="field field--date">Date :<span class="field__line"></span></span><span class="field field--time">Time :<span class="field__line"></span></span></div>
    </div>
  </section>
</body>
</html>
```